Flyer-Design für Beratungsunternehmen
Vielen Dank für die professionelle und überdurchschnittliche Unterstützung
Zielgruppe
Supervision, Coaching, Beratung
Plus digitale Beratung via App, sonstiger moderner Medien
für Organisationen, Firmen, Institutionen, Privatpersonen
Aufgabenstellung
Kreatives Design, modern, hochwertig
symphatisch, vertrauensvoll, transparent, ansprechend
Texte, Inhalte und Bilder siehe download
Sehr wichtig corporate design laut homepage www.wegweiserlotsenhaus.de

```html
<!DOCTYPE html>
<html lang="de">
<head>
<meta charset="utf-8">
<title>Flyer Lotsenhaus – Supervision, Coaching, Beratung</title>
<link href="https://fonts.googleapis.com/css2?family=Montserrat:wght@400;600;700;800&family=Raleway:wght@400;500&display=swap" rel="stylesheet">
<style>
:root{
  --green:#86bc25;
  --green-dark:#4d5c33;
  --ink:#2d2d2d;
  --text:#4a4a4a;
  --paper:#ffffff;
  --panel-grey:#f3f3f3;
  --stage:#e4e4e4;
}
*{box-sizing:border-box;margin:0;padding:0}
html,body{width:1200px;height:1200px;overflow:hidden}
body{background:var(--stage);font-family:"Raleway",sans-serif;color:var(--text);position:relative}
.spread{position:absolute;left:12px;width:1176px;height:197px;display:flex;background:var(--paper);box-shadow:0 2px 6px rgba(0,0,0,.15)}
.spread--outside{top:384px}
.spread--inside{top:617px}
.panel{position:relative;height:100%;overflow:hidden}
.h{font-family:"Montserrat",sans-serif;font-weight:700;color:var(--ink);text-transform:uppercase;letter-spacing:.6px;font-size:8.6px;text-align:center}
.divider{display:block;margin:3px auto 6px}
.small{font-size:5.6px;line-height:1.45}
.center{text-align:center}
.bold{font-family:"Montserrat",sans-serif;font-weight:700;color:var(--ink)}

/* outside */
.benefits{width:89px;background:var(--panel-grey);padding:12px 4px 0;text-align:center}
.benefits .item{font-family:"Montserrat",sans-serif;font-weight:700;color:var(--ink);font-size:5.6px;line-height:1.25}
.benefits .plus{display:block;margin:2px auto}
.benefits .claim{font-family:"Montserrat",sans-serif;font-weight:800;color:var(--green);font-size:7.8px;line-height:1.2;margin-top:6px}
.format{width:298px;padding:11px 10px 0}
.format-grid{display:flex;justify-content:space-between;margin-top:2px}
.format-grid .cell{width:68px;text-align:center}
.format-grid svg{display:block;margin:0 auto 3px}
.values{display:flex;justify-content:space-between;margin-top:4px}
.values ul{list-style:none;width:86px}
.values li{position:relative;padding-left:6px}
.values li::before{content:"›";position:absolute;left:0;top:-1px;color:var(--green);font-size:7px}
.contact{width:197px;padding:12px 16px 0 16px}
.logo{display:flex;align-items:center;gap:4px}
.logo-name{font-family:"Montserrat",sans-serif;font-weight:600;color:var(--ink);font-size:11px;letter-spacing:.4px}
.contact .logo{justify-content:center;margin:10px 0 12px}
.contact .line{display:flex;align-items:center;gap:6px;margin-top:6px}
.contact .addr{font-size:5.8px;line-height:1.4}
.photo{width:197px}
.photo-fill{position:absolute;inset:0}
.badge{position:absolute;left:10px;width:44px;background:#fff;box-shadow:0 0 2px rgba(0,0,0,.2)}
.cover{width:395px;display:flex}
.cover-text{width:200px;padding:12px 14px 0;background:linear-gradient(90deg,#fff 70%,#eeeeec);text-align:center}
.logo-box{background:#fff;box-shadow:0 1px 3px rgba(0,0,0,.18);height:50px;display:flex;align-items:center;justify-content:center}
.cover-title{font-family:"Montserrat",sans-serif;font-weight:700;color:var(--ink);font-size:11px;line-height:1.3;letter-spacing:.6px;margin-top:16px}
.signature{display:block;margin:8px auto 0;width:90px;height:18px;background:#e8f1d6;border-radius:2px}
.cover-photo{flex:1;position:relative}

/* inside */
.supervision{width:393px;padding:11px 12px 0}
.goals{background:var(--panel-grey);margin-top:7px;padding:6px 10px;display:flex;flex-wrap:wrap}
.goals .h{width:100%;text-align:left;font-size:6.6px;margin-bottom:3px}
.goals ul{list-style:none;width:50%}
.ticklist li{position:relative;padding-left:9px;margin-bottom:2px}
.ticklist li::before{content:"";position:absolute;left:0;top:1px;width:4px;height:2px;border-left:1.4px solid var(--green);border-bottom:1.4px solid var(--green);transform:rotate(-45deg)}
.formats{display:flex;justify-content:space-between;margin-top:7px;padding:0 6px}
.formats .f{width:80px;text-align:center;font-family:"Montserrat",sans-serif;font-weight:700;font-size:5.6px;color:var(--ink)}
.formats svg{display:block;margin:0 auto 3px}
.quote{width:197px;color:#fff;text-align:center}
.quote-text{position:relative;padding:38px 14px 0;font-family:"Montserrat",sans-serif;font-weight:800;font-size:8.6px;line-height:1.5;letter-spacing:.6px;text-transform:uppercase}
.quote-src{font-size:5.8px;font-weight:700;text-transform:none;letter-spacing:.2px;margin-top:10px;line-height:1.4}
.coaching{width:197px;padding:11px 14px 0;text-align:center}
.digital{width:389px;padding:11px 12px 0}
.digital-cols{display:flex;justify-content:space-between;margin-top:8px}
.digital-cols .col{width:178px}
.pluslist{list-style:none;margin-top:6px}
.pluslist li{position:relative;padding-left:11px;margin-bottom:2.5px}
.pluslist li::before{content:"+";position:absolute;left:0;top:0;width:6px;height:6px;border-radius:50%;background:var(--green);color:#fff;font:700 6px/6px "Montserrat",sans-serif;text-align:center}
.note{border-left:1.5px solid var(--green);background:var(--panel-grey);padding:4px 6px}
</style>
</head>
<body>

<svg width="0" height="0" style="position:absolute">
  <defs>
    <symbol id="divider" viewBox="0 0 40 4"><line x1="0" y1="2" x2="40" y2="2" stroke="#86bc25" stroke-width=".6"/><circle cx="20" cy="2" r="1.5" fill="#fff" stroke="#86bc25" stroke-width=".6"/></symbol>
    <symbol id="plus" viewBox="0 0 10 10"><circle cx="5" cy="5" r="5" fill="#86bc25"/><path d="M5 2.5v5M2.5 5h5" stroke="#fff" stroke-width="1.4"/></symbol>
    <symbol id="tickbox" viewBox="0 0 14 14"><rect x="1" y="3" width="10" height="10" rx="1.5" fill="none" stroke="#86bc25" stroke-width="1.4"/><path d="M3.5 7.5l2.5 2.5 6.5-8" fill="none" stroke="#86bc25" stroke-width="1.8"/></symbol>
    <symbol id="mark" viewBox="0 0 10 10"><rect width="10" height="10" fill="#86bc25"/></symbol>
  </defs>
</svg>

<!-- Outside spread -->
<section class="spread spread--outside">
  <div class="panel benefits">
    <div class="h" style="font-size:7.6px">Ihre Vorzüge</div>
    <svg class="divider" width="30" height="4"><use href="#divider"/></svg>
    <div class="item">Effizienz</div><svg class="plus" width="6" height="6"><use href="#plus"/></svg>
    <div class="item">Mobilität</div><svg class="plus" width="6" height="6"><use href="#plus"/></svg>
    <div class="item">Flexibilität</div><svg class="plus" width="6" height="6"><use href="#plus"/></svg>
    <div class="item">Nachhaltigkeit</div><svg class="plus" width="6" height="6"><use href="#plus"/></svg>
    <div class="item">Sicherheit</div><svg class="plus" width="6" height="6"><use href="#plus"/></svg>
    <div class="item">großmögliche<br>Anonymität</div>
    <div class="claim">SPAREN SIE ZEIT<br>UND GELD!</div>
  </div>

  <div class="panel format">
    <div class="h">Mein Format für Ihren Mehrwert!</div>
    <svg class="divider" width="40" height="4"><use href="#divider"/></svg>
    <div class="format-grid small">
      <div class="cell"><svg width="13" height="13"><use href="#tickbox"/></svg>Nachhaltiger Erfolg durch digitale Begleitung</div>
      <div class="cell"><svg width="13" height="13"><use href="#tickbox"/></svg>Roter Faden des Veränderungs&shy;prozesses sichtbar</div>
      <div class="cell"><svg width="13" height="13"><use href="#tickbox"/></svg>Zeit- &amp; Orts&shy;unabhängiges Coaching</div>
      <div class="cell"><svg width="13" height="13"><use href="#tickbox"/></svg>Beste Transfer- &amp; Nachbegleitung</div>
    </div>
    <div class="h" style="margin-top:20px">Meine Werte &amp; Haltung</div>
    <svg class="divider" width="40" height="4"><use href="#divider"/></svg>
    <div class="values small">
      <ul><li>Wertschätzung, Ressourcenorientierung und Respekt</li><li>Systemisch</li><li>Lösungsorientiert</li></ul>
      <ul><li>Kompetenz und Methodenvielfalt</li><li>Nicht für, sondern mit Ihnen!</li></ul>
      <ul><li>Transparenz und Struktur</li><li>Verschwiegenheit und Vertrauen</li></ul>
    </div>
  </div>

  <div class="panel contact">
    <div class="logo"><svg width="11" height="11"><use href="#mark"/></svg><span class="logo-name">LOTSENHAUS</span></div>
    <div class="addr"><span class="bold">Ida Brunkel</span><br>Lindenweg 12<br>35037 Marburg an der Lahn</div>
    <div class="line" style="margin-top:12px">
      <svg width="14" height="14" viewBox="0 0 14 14"><path d="M3 1.5l2.3 2.8-1.4 1.6c.9 2 2.2 3.3 4.2 4.2l1.6-1.4 2.8 2.3-1.5 1.8C6.6 12.6 1.4 7.4 1.2 3z" fill="none" stroke="#86bc25" stroke-width="1"/></svg>
      <div class="addr">Rufen Sie mich an!<br><span class="bold">0151 482 17 63</span></div>
    </div>
    <div class="line">
      <svg width="14" height="14" viewBox="0 0 14 14" fill="none" stroke="#86bc25" stroke-width=".9"><circle cx="7" cy="7" r="6"/><ellipse cx="7" cy="7" rx="2.6" ry="6"/><path d="M1 7h12M2 4h10M2 10h10"/></svg>
      <div class="addr">Web<br><span class="bold">www.wegweiserlotsenhaus.de</span></div>
    </div>
    <div class="line">
      <svg width="14" height="14" viewBox="0 0 14 14" fill="none" stroke="#86bc25" stroke-width=".9"><path d="M1 6l6-4.5L13 6v7H1z"/><path d="M1 6l6 4 6-4"/></svg>
      <div class="addr">E-Mail<br><span class="bold">info@wegweiserlotsenhaus.de</span></div>
    </div>
  </div>

  <div class="panel photo">
    <div class="photo-fill" role="img" aria-label="Porträtfoto der Beraterin am Laptop in einem hellen Büro" style="background:linear-gradient(135deg,#c9ccc9,#8a8f94 55%,#2f3b5a)"></div>
    <div class="badge" style="top:10px;height:26px"></div>
    <div class="badge" style="top:46px;height:26px"></div>
  </div>

  <div class="panel cover">
    <div class="cover-text">
      <div class="logo-box"><div class="logo"><svg width="11" height="11"><use href="#mark"/></svg><span class="logo-name">LOTSENHAUS</span></div></div>
      <div class="cover-title">Supervision -<br>Coaching - Beratung</div>
      <p class="small" style="margin-top:5px">Mit meiner individuellen Begleitung können Sie Herausforderungen sicher meistern.</p>
      <span class="signature" role="img" aria-label="Handschriftliche Unterschrift der Beraterin"></span>
    </div>
    <div class="cover-photo" role="img" aria-label="Porträtfoto der Beraterin in schwarzer Bluse vor hellem Hintergrund" style="background:linear-gradient(90deg,#eeeeec,#dcdedb 40%,#3a3a3a 75%,#d5d7d3)"></div>
  </div>
</section>

<!-- Inside spread -->
<section class="spread spread--inside">
  <div class="panel supervision">
    <div class="h">Systemische Supervision</div>
    <svg class="divider" width="40" height="4"><use href="#divider"/></svg>
    <p class="small center">bietet Ihnen und Ihrem Team einen geschützten Raum Ihren Arbeitskontext, komplexe Anforderungen und Strukturen moderiert zu reflektieren sowie Konflikte, Rollen und Fragestellungen zu klären.</p>
    <div class="goals small">
      <div class="h">Ziele</div>
      <ul class="ticklist"><li>Rollensicherheit und Teamfähigkeit weiterentwickeln</li><li>tiefes Verständnis der beruflichen Situation, Handlungsmöglichkeiten und Perspektiven entwickeln</li></ul>
      <ul class="ticklist"><li>Qualitätssicherung</li><li>Stärken &amp; Kompetenzen bewusst machen</li><li>langfristig die Freude an Ihrer Arbeit erhalten</li></ul>
    </div>
    <div class="formats">
      <div class="f"><svg width="18" height="18" viewBox="0 0 18 18" fill="#86bc25"><circle cx="9" cy="5" r="4"/><path d="M2 18c0-5 3-7.5 7-7.5s7 2.5 7 7.5z"/></svg>Einzelsupervision</div>
      <div class="f"><svg width="24" height="18" viewBox="0 0 24 18" fill="#86bc25"><circle cx="12" cy="5" r="3.5"/><circle cx="5" cy="7" r="3"/><circle cx="19" cy="7" r="3"/><path d="M5 18c0-5 3-7 7-7s7 2 7 7z"/><path d="M0 17c0-4 2-6 5-6 1 0 2 .3 2.5.8L5 17zM24 17c0-4-2-6-5-6-1 0-2 .3-2.5.8L19 17z"/></svg>Gruppensupervision</div>
      <div class="f"><svg width="14" height="18" viewBox="0 0 14 18"><rect width="14" height="18" fill="#86bc25"/><g fill="#fff"><rect x="3" y="3" width="2" height="2"/><rect x="6" y="3" width="2" height="2"/><rect x="9" y="3" width="2" height="2"/><rect x="3" y="7" width="2" height="2"/><rect x="6" y="7" width="2" height="2"/><rect x="9" y="7" width="2" height="2"/><rect x="3" y="11" width="2" height="2"/><rect x="9" y="11" width="2" height="2"/><rect x="6" y="13" width="2" height="5"/></g></svg>Teamsupervision</div>
      <div class="f"><svg width="20" height="18" viewBox="0 0 20 18" fill="#86bc25"><rect x="9" y="0" width="2" height="18"/><path d="M2 2h15l3 2.5L17 7H2z"/><path d="M18 9H3L0 11.5 3 14h15z"/></svg>Fallsupervision</div>
    </div>
  </div>

  <div class="panel quote">
    <div class="photo-fill" role="img" aria-label="Foto einer Gruppe im Gesprächskreis von oben, grün eingefärbt" style="background:radial-gradient(circle at 50% 55%,#5f6e44,#3e4b2a 70%)"></div>
    <div class="quote-text">„Zusammenkommen ist ein Beginn, zusammenbleiben ein Fortschritt, zusammenarbeiten ein Erfolg.“
      <div class="quote-src">Jonas Weidtmann –<br>Unternehmer</div>
    </div>
  </div>

  <div class="panel coaching">
    <div class="h">Systemisches Coaching</div>
    <svg class="divider" width="40" height="4"><use href="#divider"/></svg>
    <p class="small">Erweitern Sie Ihre beruflichen Handlungsstrategien und machen Sie Ihre Stärken und Fähigkeiten nutzbar, um Ihr Ziel zu erreichen. Persönliche Zufriedenheit und professionelle Leistungsfähigkeit stehen im Fokus.</p>
    <div class="h" style="margin-top:10px">Lifecoaching</div>
    <svg class="divider" width="40" height="4"><use href="#divider"/></svg>
    <p class="small">Im Mittelpunkt stehen Ihre persönlichen Sorgen, Wünsche und Anliegen. Gemeinsam erarbeiten wir Ihr konkretes Ziel und gehen auf Schatzsuche, entdecken neue Perspektiven, Handlungsoptionen, die Sie Schritt für Schritt Ihrem persönlichen Erfolg näherbringen.</p>
  </div>

  <div class="panel digital">
    <div class="h">Digitale Beratung</div>
    <svg class="divider" width="40" height="4"><use href="#divider"/></svg>
    <p class="small center">Endlich können Sie ganz einfach ungenutzte Zeit auf dem Weg zur Arbeit, in Wartebereichen oder Zwischendurch nutzen, um Ihre Ziele und Wünsche wahr werden zu lassen.</p>
    <div class="digital-cols small">
      <div class="col">
        <div class="h" style="text-align:left;font-size:7px;margin-top:12px">Bei mir erhalten Sie</div>
        <ul class="pluslist">
          <li>Eigenen geschützten Account / eigene App</li>
          <li>24 Stunden / 7 Tage in der Woche Zugang</li>
          <li>Visualisierung Ihrer Erfolge</li>
          <li>Eine Vielzahl an Tools und Fragebögen zur konkreten Umsetzungsbegleitung</li>
          <li>Responsive Design / nutzbar auf dem Smartphone, Tablet, PC</li>
          <li>Höchstmaß an Flexibilität</li>
        </ul>
      </div>
      <div class="col">
        <div class="note">Entscheiden Sie selbst, ob Sie die Möglichkeit der digitalen Beratung zusätzlich nutzen wollen oder diese die Sitzungen vor Ort komplett ersetzen soll.</div>
        <p class="bold" style="margin-top:9px">Sie möchten auf die klassischen Sitzungen nicht verzichten?</p>
        <p style="margin-top:3px;text-align:justify">Nutzen Sie die digitale Begleitung dazwischen und / oder nach dem gesamten Beratungsprozess (Follow-Up). So sichern Sie Ihre Erfolge auch langfristig und brauchen vor Herausforderungen und Widerständen im Alltag keine Angst mehr haben.</p>
      </div>
    </div>
  </div>
</section>

</body>
</html>
```